Business card design needed

We need a business card for a consulting company called Harbor Business Consulting which covers a range of business services in construction and Human Resources. We have chosen balck and red as the colours and have an idea for the logo of a person with arms outstretched signifying all encompassing. See attachment.
Industry/Entity Type
Construction
Contact Information for Business Card
Dennis Holloway
Business Consultant/Project Manager/ Experienced Builder (Dip Bdg & Construction)
Mobile: 0481 362 954
Email: dennisholloway@harborconsulting.com.au
PO Box 7814
Kelvin Heights, NSW, 2830, Australia
Logo Text
Harbor Business Consulting
Look and feel

```html
<!DOCTYPE html>
<html lang="en">
<head>
<meta charset="utf-8">
<title>Harbor Business Consulting – Business Card</title>
<link rel="stylesheet" href="https://fonts.googleapis.com/css2?family=Arimo:wght@400;700&family=Questrial&display=swap">
<style>
  :root {
    --stage: #b9b9b9;
    --ink: #0b0b0b;
    --ink-soft: #1f1f21;
    --red: #d8141c;
    --red-deep: #a80d12;
    --paper: #ffffff;
    --text-light: #f2f2f2;
  }
  * { box-sizing: border-box; margin: 0; padding: 0; }
  html, body {
    width: 1200px; height: 900px; overflow: hidden;
    background: var(--stage);
  }
  .sheet {
    position: relative; width: 1200px; height: 900px;
    display: flex; align-items: center; justify-content: center; gap: 40px;
  }
  .card {
    position: relative; width: 560px; height: 320px; overflow: hidden;
    font-family: "Questrial", "Arimo", sans-serif;
  }

  .brand__mark { border-radius: 50%; background: var(--red); flex: none; display: block; }
  .brand__name {
    font-family: "Questrial", sans-serif; font-weight: 400; color: var(--red);
    white-space: nowrap;
  }

  /* Back of card: services */
  .card--back {
    background: radial-gradient(ellipse at 50% 30%, var(--ink-soft) 0%, var(--ink) 70%);
    color: var(--text-light);
  }
  .card--back .brand {
    display: flex; flex-direction: column; align-items: center; gap: 8px;
    padding-top: 22px;
  }
  .card--back .brand__mark { width: 62px; height: 62px; }
  .card--back .brand__name { font-size: 34px; letter-spacing: 0.5px; }

  .services {
    display: flex; justify-content: space-between;
    padding: 12px 26px 0 22px;
  }
  .service-list { list-style: none; font-family: "Arimo", sans-serif; }
  .service-list li {
    position: relative; padding-left: 11px; line-height: 1.16;
  }
  .service-list li::before {
    content: ""; position: absolute; left: 0; top: 0.5em;
    width: 4px; height: 4px; border-radius: 50%; background: var(--red);
  }
  .service-list--work { font-size: 13.5px; }
  .service-list--sectors { font-size: 16px; width: 210px; padding-top: 10px; }

  /* Front of card: contact */
  .card--front { background: var(--ink); color: var(--text-light); }
  .front__head {
    height: 150px; background: var(--paper);
    display: flex; align-items: center; padding-left: 28px;
  }
  .card--front .brand { display: flex; align-items: center; gap: 14px; }
  .card--front .brand__mark { width: 116px; height: 116px; }
  .card--front .brand__name { font-size: 26px; }
  .front__stripe { height: 10px; background: linear-gradient(var(--red), var(--red-deep)); }
  .front__body {
    height: 160px; padding: 14px 24px 0 28px;
    background: linear-gradient(180deg, var(--ink-soft) 0%, var(--ink) 100%);
  }
  .person__name { font-size: 19px; color: var(--text-light); }
  .person__title { font-size: 11px; color: var(--red); margin-top: 2px; white-space: nowrap; }
  .contact {
    display: grid; grid-template-columns: 64px 1fr; row-gap: 2px;
    margin-top: 22px; font-size: 17px;
  }
  .contact__label { color: var(--red); }
  .contact__value { color: var(--text-light); white-space: nowrap; }
  .contact__value--address { grid-column: 2; }
</style>
</head>
<body>
<main class="sheet">

  <section class="card card--back" aria-label="Card back: services">
    <div class="brand">
      <span class="brand__mark" aria-hidden="true"></span>
      <span class="brand__name">Harbor Business Consulting</span>
    </div>
    <div class="services">
      <ul class="service-list service-list--work">
        <li>Project Management</li>
        <li>Costruction Design Advice/Mgmt</li>
        <li>Estimating Services(Construction)</li>
        <li>Building Site Supervision</li>
        <li>Management of Building Maintenance</li>
        <li>Site relocations</li>
        <li>Subcontractor Management</li>
      </ul>
      <ul class="service-list service-list--sectors">
        <li>Medical/Health</li>
        <li>Commercial &amp; Industrial</li>
        <li>Retail/Hospitality</li>
        <li>Community/Sport Facilities</li>
        <li>Educational facilities</li>
        <li>Multi-Unit Residential</li>
        <li>Domestic</li>
      </ul>
    </div>
  </section>

  <section class="card card--front" aria-label="Card front: contact details">
    <header class="front__head">
      <div class="brand">
        <span class="brand__mark" aria-hidden="true"></span>
        <span class="brand__name">Harbor Business Consulting</span>
      </div>
    </header>
    <div class="front__stripe"></div>
    <div class="front__body">
      <p class="person__name">Dennis Holloway</p>
      <p class="person__title">Business Consultant/Project Manager/ Experienced Builder (Dip Bdg &amp; Construction)</p>
      <div class="contact">
        <span class="contact__label">Mobile:</span>
        <span class="contact__value">0481 362 954</span>
        <span class="contact__label">Email:</span>
        <span class="contact__value">dennisholloway@harborconsulting.com.au</span>
        <span class="contact__value contact__value--address">PO Box 7814 Kelvin Heights, NSW, 2830, Australia</span>
      </div>
    </div>
  </section>

</main>
</body>
</html>
```